Visitenkarten-Design für private Praxis für Sprachtherapie
Zielgruppe
Private Praxis für Sprachtherapie (Logopädie)
Aufgabenstellung
Siehe PDF der Anlage.

```html
<!DOCTYPE html>
<html lang="de">
<head>
<meta charset="utf-8">
<title>Visitenkarte – Praxis für Sprachtherapie</title>
<link rel="stylesheet" href="https://fonts.googleapis.com/css2?family=Fira+Sans+Condensed:wght@400;500;600&display=swap">
<style>
  :root {
    --navy: #13214f;
    --mid-blue: #5878b4;
    --card-bg: #e9f5fc;
    --wave: #d5ebf8;
    --field: #ffffff;
    --page-bg: #f5f8fb;
  }
  * { margin: 0; padding: 0; box-sizing: border-box; }
  html, body { width: 1200px; height: 1200px; overflow: hidden; }
  body {
    background: linear-gradient(135deg, #ffffff 0%, var(--page-bg) 60%, #f1f5fa 100%);
    font-family: "Fira Sans Condensed", sans-serif;
    color: var(--navy);
    position: relative;
  }
  .card {
    position: absolute;
    top: 266px;
    width: 432px;
    height: 667px;
    background: var(--card-bg);
    overflow: hidden;
    box-shadow: 2px 3px 8px rgba(19, 33, 79, 0.18);
  }
  .card--front { left: 145px; }
  .card--back { left: 623px; }

  .wave-area {
    position: absolute;
    right: 0;
    bottom: 0;
    width: 330px;
    height: 380px;
    background: radial-gradient(ellipse at 80% 70%, var(--wave) 0%, var(--wave) 45%, rgba(213,235,248,0) 75%);
  }

  /* Front */
  .brand {
    position: absolute;
    left: 64px;
    top: 86px;
    display: flex;
    align-items: center;
    gap: 14px;
  }
  .brand__text {
    font-weight: 600;
    font-size: 23px;
    line-height: 1.15;
    color: var(--navy);
  }
  .brand__dot {
    width: 44px; height: 44px;
    border-radius: 50%;
    background: var(--navy);
  }
  .practice {
    position: absolute;
    left: 0; right: 0;
    top: 236px;
    text-align: center;
    font-weight: 600;
    font-size: 33px;
    line-height: 39px;
  }
  .address {
    position: absolute;
    left: 0; right: 0;
    top: 326px;
    text-align: center;
    font-size: 26px;
    line-height: 33px;
  }
  .contact {
    position: absolute;
    left: 0; right: 0;
    top: 472px;
    list-style: none;
    font-size: 26px;
    line-height: 39px;
  }
  .contact li {
    display: flex;
    justify-content: center;
    align-items: center;
    gap: 8px;
  }
  .contact svg { fill: var(--mid-blue); }
  .band-light {
    position: absolute; left: 0; right: 0;
    top: 616px; height: 14px;
    background: var(--mid-blue);
  }
  .band-dark {
    position: absolute; left: 0; right: 0;
    top: 630px; bottom: 0;
    background: var(--navy);
  }

  /* Back */
  .field {
    position: absolute;
    left: 0; right: 0;
    height: 47px;
  }
  .field__label {
    position: absolute;
    left: 26px;
    top: 50%;
    transform: translateY(-50%);
    font-size: 19px;
    line-height: 19px;
    color: #111;
  }
  .field__box {
    position: absolute;
    left: 151px;
    width: 261px;
    top: 0; bottom: 0;
    background: var(--field);
  }
  .schedule__title {
    position: absolute;
    left: 0; right: 0;
    top: 262px;
    text-align: center;
    font-weight: 600;
    font-size: 28px;
  }
  .col {
    position: absolute;
    top: 302px;
  }
  .col--day { left: 19px; width: 137px; }
  .col--date { left: 168px; width: 96px; }
  .col--time { left: 275px; width: 137px; }
  .col__head {
    height: 41px;
    background: var(--navy);
    color: #fff;
    font-size: 23px;
    line-height: 38px;
    text-align: center;
  }
  .col__cell {
    height: 50px;
    margin-top: 10.5px;
    background: rgba(255,255,255,0.8);
  }
</style>
</head>
<body>

<section class="card card--front">
  <div class="wave-area" role="img" aria-label="Sanfte hellblaue Wellenfläche als Hintergrund"></div>

  <div class="brand">
    <div class="brand__text">Praxis für Sprachtherapie<br>Henrike Vossberg</div>
    <span class="brand__dot"></span>
  </div>

  <h1 class="practice">Praxis für Sprachtherapie<br>Henrike Vossberg</h1>
  <p class="address">Kastanienweg 14<br>32105 Bad Salzuflen</p>

  <ul class="contact">
    <li>
      <svg width="20" height="20" viewBox="0 0 24 24" aria-hidden="true"><path d="M6.6 10.8a15.1 15.1 0 0 0 6.6 6.6l2.2-2.2c.3-.3.7-.4 1-.2 1.1.4 2.3.6 3.6.6.6 0 1 .4 1 1V20c0 .6-.4 1-1 1A17 17 0 0 1 3 4c0-.6.4-1 1-1h3.5c.6 0 1 .4 1 1 0 1.3.2 2.5.6 3.6.1.3 0 .7-.2 1z"/></svg>
      <span>05222 480916</span>
    </li>
    <li>
      <svg width="22" height="16" viewBox="0 0 22 16" aria-hidden="true"><path d="M0 0h22v2L11 9 0 2z"/><path d="M0 4l11 7 11-7v12H0z"/></svg>
      <span>info@logopaedie-vossberg.de</span>
    </li>
    <li>
      <svg width="20" height="20" viewBox="0 0 20 20" aria-hidden="true"><path d="M10 0a10 10 0 1 0 0 20 10 10 0 0 0 0-20zm0 2c.9 0 2 1.7 2.5 5h-5C8 3.7 9.1 2 10 2zM2.3 9h3.2c0 .7 0 1.4.1 2H2.3a8 8 0 0 1 0-2zm5.2 2a18 18 0 0 1 0-2h5a18 18 0 0 1 0 2zm7-2h3.2a8 8 0 0 1 0 2h-3.3c.1-.6.1-1.3.1-2zM10 18c-.9 0-2-1.7-2.5-5h5c-.5 3.3-1.6 5-2.5 5z"/></svg>
      <span>logopaedie-vossberg.de</span>
    </li>
  </ul>

  <div class="band-light"></div>
  <div class="band-dark"></div>
</section>

<section class="card card--back">
  <div class="wave-area" role="img" aria-label="Sanfte hellblaue Wellenfläche als Hintergrund"></div>

  <div class="field" style="top:24px"><span class="field__label">Vor- und<br>Nachname</span><span class="field__box"></span></div>
  <div class="field" style="top:81px"><span class="field__label">Funktion</span><span class="field__box"></span></div>
  <div class="field" style="top:139px"><span class="field__label">Telefonnummer</span><span class="field__box"></span></div>
  <div class="field" style="top:196px"><span class="field__label">E-Mail-Adresse</span><span class="field__box"></span></div>

  <h2 class="schedule__title">Ihr nächsten Termin</h2>

  <div class="col col--day">
    <div class="col__head">Wochentag</div>
    <div class="col__cell"></div><div class="col__cell"></div><div class="col__cell"></div><div class="col__cell"></div><div class="col__cell"></div>
  </div>
  <div class="col col--date">
    <div class="col__head">Datum</div>
    <div class="col__cell"></div><div class="col__cell"></div><div class="col__cell"></div><div class="col__cell"></div><div class="col__cell"></div>
  </div>
  <div class="col col--time">
    <div class="col__head">Uhrzeit</div>
    <div class="col__cell"></div><div class="col__cell"></div><div class="col__cell"></div><div class="col__cell"></div><div class="col__cell"></div>
  </div>
</section>

</body>
</html>
```